Brightbay Business Card Design

Our company is called Brightbay. We manufacture confectionary snacks & frozen novelties. Our initial product portfolio includes frozen ice lollies/popsicles & stick ice cream bars.

We require a business card design.

Please use the attached Logo.

Please use an orange, brown, yellow colour code. You may choose any combination of the 3 or include all three. The logo however must remain orange.

Target Market(s)

Business card will be targeted at distributors of our products such as supermarket procurement managers, convenience store owners, wholesale distributors and merchandising agents.

Industry/Entity Type

Business

Requirements
Must have
• Calvin Obeng_Director/ P.O.Box Dunmore 5172, Accra, Ghana / m: 00233(0)507318924/ e: calvin.obeng@mailvora.co.uk

```html
<!DOCTYPE html>
<html lang="en">
<head>
<meta charset="utf-8">
<title>Brightbay Business Card</title>
<link rel="stylesheet" href="https://fonts.googleapis.com/css2?family=Encode+Sans+Condensed:wght@400;700&display=swap">
<style>
  :root {
    --bg-top: #d6c9ba;
    --bg-mid: #f1ede9;
    --bg-low: #ebe6e1;
    --brand-orange: #f07a32;
    --brand-yellow: #fcdc1c;
    --brand-brown: #5c432b;
    --band-dark: #5e4630;
    --band-light: #f3f0ec;
    --text-brown: #5a4431;
  }
  * { margin: 0; padding: 0; box-sizing: border-box; }
  html, body {
    width: 1200px;
    height: 705px;
    overflow: hidden;
    background: #ffffff;
  }
  .card {
    position: relative;
    width: 1200px;
    height: 705px;
    overflow: hidden;
    background: linear-gradient(180deg, var(--bg-top) 0%, var(--bg-mid) 55%, var(--bg-low) 100%);
    font-family: "Encode Sans Condensed", "Arial Narrow", sans-serif;
    color: var(--text-brown);
  }
  .holder {
    position: absolute;
    top: 28px;
    right: 33px;
    text-align: right;
    font-size: 29px;
    line-height: 46px;
  }
  .holder .phone {
    display: inline-flex;
    align-items: center;
    gap: 8px;
  }
  .icon { fill: var(--text-brown); flex: none; }
  .brand {
    position: absolute;
    left: 0;
    right: 0;
    top: 210px;
    display: flex;
    justify-content: center;
    align-items: center;
    gap: 22px;
  }
  .brand-dot {
    width: 58px;
    height: 58px;
    border-radius: 50%;
    background: var(--brand-orange);
  }
  .brand-name {
    font-size: 130px;
    font-weight: 700;
    line-height: 1;
    color: var(--brand-orange);
  }
  .wave {
    position: absolute;
    left: 0;
    top: 0;
  }
  .contact {
    position: absolute;
    left: 0;
    right: 0;
    top: 586px;
    text-align: center;
    font-size: 29px;
    line-height: 48px;
  }
  .contact-line {
    display: flex;
    justify-content: center;
    align-items: center;
    gap: 6px;
  }
</style>
</head>
<body>
<div class="card">
  <svg class="wave" width="1200" height="705" viewBox="0 0 1200 705" aria-hidden="true">
    <defs>
      <linearGradient id="bandShade" x1="0" y1="0" x2="1" y2="0">
        <stop offset="0" stop-color="var(--band-dark)"/>
        <stop offset="0.5" stop-color="var(--band-light)"/>
        <stop offset="1" stop-color="var(--band-dark)"/>
      </linearGradient>
    </defs>
    <path fill="var(--brand-orange)" d="M0,552 C90,470 180,440 300,452 C450,468 570,530 730,532 C900,534 1050,490 1200,458 L1200,705 L0,705 Z"/>
    <path fill="var(--brand-yellow)" transform="translate(0,7)" d="M0,552 C90,470 180,440 300,452 C450,468 570,530 730,532 C900,534 1050,490 1200,458 L1200,705 L0,705 Z"/>
    <path fill="var(--brand-brown)" transform="translate(0,13)" d="M0,552 C90,470 180,440 300,452 C450,468 570,530 730,532 C900,534 1050,490 1200,458 L1200,705 L0,705 Z"/>
    <path fill="url(#bandShade)" transform="translate(0,19)" d="M0,552 C90,470 180,440 300,452 C450,468 570,530 730,532 C900,534 1050,490 1200,458 L1200,705 L0,705 Z"/>
  </svg>

  <div class="holder">
    <div class="name">Calvin Obeng</div>
    <div class="role">Director</div>
    <div class="phone">
      <svg class="icon" width="20" height="28" viewBox="0 0 20 28" aria-hidden="true">
        <path d="M3,0 H17 A3,3 0 0 1 20,3 V25 A3,3 0 0 1 17,28 H3 A3,3 0 0 1 0,25 V3 A3,3 0 0 1 3,0 Z M3,3 V20 H17 V3 Z M8,22 V25 H12 V22 Z" fill-rule="evenodd"/>
      </svg>
      <span>: 00233(0)507318924</span>
    </div>
  </div>

  <div class="brand">
    <span class="brand-dot"></span>
    <span class="brand-name">Brightbay</span>
  </div>

  <div class="contact">
    <div class="contact-line">
      <svg class="icon" width="18" height="26" viewBox="0 0 18 26" aria-hidden="true">
        <path d="M9,0 A9,9 0 0 1 18,9 C18,16 9,26 9,26 C9,26 0,16 0,9 A9,9 0 0 1 9,0 Z M9,5 A4,4 0 1 0 9,13 A4,4 0 1 0 9,5 Z" fill-rule="evenodd"/>
      </svg>
      <span>: P.O.Box Dunmore 5172, Accra, Ghana</span>
    </div>
    <div class="contact-line">
      <svg width="34" height="26" viewBox="0 0 34 26" aria-hidden="true" fill="none" stroke="var(--text-brown)" stroke-width="2.4" stroke-linejoin="round">
        <path d="M2,11 L17,2 L32,11 V24 H2 Z"/>
        <path d="M2,11 L17,19 L32,11"/>
        <path d="M2,24 L13,16 M32,24 L21,16"/>
      </svg>
      <span>: calvin.obeng@mailvora.co.uk</span>
    </div>
  </div>
</div>
</body>
</html>
```